folding sales brochure

We need a brochure in the colors of orange, black and charcoal gray - our logo colors.
www.venmoretranslinks

Strong, clean - and something eye catching.

We are looking for graphic images and photos that depict international business, written translation, live simultaneous interpretation for conferences & events with people communicating. We have some photos, but are open to others.

This brochure will generalize our companies services.
This brochure will be used for B2B as well as Trade Show booths.

Reason: Project has been extended to allow time for feedback and completion. Thank you all... some wonderful designs.

Thank you all for your designs - they were all creative in so many different ways, making the choice of just one very difficult.

regards,
Harriet

Target Market(s)

Our target is large global corporate companies.

Industry/Entity Type

Events

Requirements
Must have
• company logo (will supply)
company website and address etc.

Our Type Font is: Helvetica Neue LT Std

All info needed can be found here: www.venmoretranslinks
Should not have
• we feel globes and flags are overdone in the International marketplace - hopefully you can find something else to speak Global.

```html
<!DOCTYPE html>
<html lang="en">
<head>
<meta charset="utf-8">
<title>Venmore Translinks – Folding Brochure, Inside Spread</title>
<link href="https://fonts.googleapis.com/css2?family=Inter:wght@400;500;700&display=swap" rel="stylesheet">
<style>
  :root {
    --orange: #f08a2c;
    --orange-deep: #e5761b;
    --orange-light: #f7a24e;
    --charcoal: #4a4b50;
    --ink: #1c1c1c;
    --body-text: #555555;
    --label-gray: #b9b9b9;
    --frame: #555555;
    --paper-top: #dedede;
    --paper-bottom: #ffffff;
    --white: #ffffff;
  }
  * { box-sizing: border-box; margin: 0; padding: 0; }
  html, body { width: 1200px; height: 898px; overflow: hidden; background: var(--white); }
  body { position: relative; font-family: "Inter", Helvetica, Arial, sans-serif; color: var(--body-text); }

  .panel-label {
    position: absolute; top: 6px; width: 580px; text-align: center;
    font-size: 21px; color: var(--label-gray); font-weight: 400;
  }
  .panel-label--left { left: 20px; }
  .panel-label--right { left: 605px; }

  .spread {
    position: absolute; left: 17px; top: 36px; width: 1166px; height: 824px;
    border: 1px solid var(--frame); overflow: hidden;
  }
  .page {
    position: absolute; top: 0; width: 583px; height: 100%;
    background: linear-gradient(180deg, var(--paper-top) 0%, var(--paper-bottom) 45%, #f2f2f2 100%);
  }
  .page--left { left: 0; border-right: 1px solid var(--frame); }
  .page--right { left: 583px; }

  .photo { position: absolute; }

  .section-title {
    position: absolute; font-size: 14px; font-weight: 700; color: var(--ink);
    display: flex; align-items: center; gap: 6px; white-space: nowrap;
  }
  .dots { display: inline-block; }

  .body-copy {
    position: absolute; font-size: 9.6px; line-height: 15px; text-align: justify;
  }

  .feature-title {
    position: absolute; left: 882px; top: 140px; font-size: 23px; line-height: 28px;
    font-weight: 400; color: var(--ink); letter-spacing: 0.3px;
  }

  .band {
    position: absolute; top: 514px; height: 214px; width: 583px;
  }
  .band__panel {
    position: absolute; top: 0; left: 0; height: 100%; background: var(--orange);
    color: var(--white); font-size: 18.5px; line-height: 23.5px; letter-spacing: 0.3px;
  }
  .band__panel p { position: absolute; left: 21px; }
  .band__photo { position: absolute; top: 0; height: 100%; }

  .rule { position: absolute; top: 728px; height: 6px; width: 583px; background: #c9c9c9; }
  .footer-band {
    position: absolute; top: 734px; height: 76px; width: 583px; overflow: hidden;
    background: var(--orange);
  }
  .footer-band svg { position: absolute; left: 0; top: 0; }
  .web-address {
    position: absolute; left: 0; width: 100%; top: 30px; text-align: center;
    color: var(--white); font-size: 12.5px; letter-spacing: 0.2px;
  }
  .base-strip { position: absolute; top: 810px; height: 14px; width: 583px; background: var(--charcoal); }
</style>
</head>
<body>

<div class="panel-label panel-label--left">Inside left</div>
<div class="panel-label panel-label--right">Inside Right</div>

<div class="spread">
  <!-- Inside left page -->
  <section class="page page--left">
    <h2 class="section-title" style="left:35px; top:52px;">Language solutions for today
      <svg class="dots" width="40" height="14" viewBox="0 0 40 14"><circle cx="5" cy="7" r="4.5" fill="var(--orange)"/><circle cx="19" cy="7" r="5.5" fill="var(--orange-light)"/><circle cx="33" cy="7" r="3" fill="var(--orange)"/></svg>
    </h2>
    <p class="body-copy" style="left:35px; top:80px; width:251px;">“Language Solutions” are the services that allow communication to transcend language barriers. We begin with translators and interpreters and finish with the technology to bring it all together. Our solutions are just that: answers to problems. We meet your needs so you don't have to worry. Through Venmore, youcommunicate with your global audience with equal respect. We are a nationwide leader in live event language services, which includes simultaneous interpreters, interpreting equipment, and push-to-talk discussion systems. Our translation division has decades of experience and millions of words under its belt. Today, these services include a full range of studio services like voiceover and subtitles.</p>
    <div class="photo" role="img" aria-label="Technician at a control desk facing a wall of broadcast monitors" style="left:312px; top:84px; width:232px; height:150px; background:linear-gradient(135deg,#1a1f2a,#3d4f6a 50%,#12151c);"></div>

    <h2 class="section-title" style="right:31px; top:333px;">
      <svg class="dots" width="40" height="14" viewBox="0 0 40 14"><circle cx="5" cy="7" r="3" fill="var(--orange)"/><circle cx="19" cy="7" r="5.5" fill="var(--orange-light)"/><circle cx="33" cy="7" r="4.5" fill="var(--orange)"/></svg>Language solutions for today</h2>
    <div class="photo" role="img" aria-label="Conference table with interpretation headsets and receivers" style="left:35px; top:360px; width:212px; height:138px; background:linear-gradient(135deg,#6b4a2a,#c9a27a 55%,#e8dccb);"></div>
    <p class="body-copy" style="left:289px; top:360px; width:263px;">“Language Solutions” are the services that allow communication to transcend language barriers. We begin with translators and interpreters and finish with the technology to bring it all together. Our solutions are just that: answers to problems. We meet your needs so you don't have to worry. Through Venmore, youcommunicate with your global audience with equal respect.</p>

    <div class="band">
      <div class="band__panel" style="width:214px;">
        <p style="top:62px;">LIVE EVENT<br>INTERPRETATION,<br>UNLIMITED<br>LANGUAGES
          <svg width="40" height="14" viewBox="0 0 40 14"><circle cx="6" cy="7" r="4.5" fill="var(--white)"/><circle cx="20" cy="7" r="5.5" fill="var(--white)"/><circle cx="33" cy="7" r="3" fill="var(--white)"/></svg></p>
      </div>
      <div class="band__photo" role="img" aria-label="Ballroom with a row of interpreter booths" style="left:214px; width:369px; background:linear-gradient(160deg,#3a1d3a,#7a4a7a 40%,#2a1a2a 75%,#4a2a30);"></div>
    </div>
    <div class="rule"></div>
    <div class="footer-band">
      <svg width="583" height="76" viewBox="0 0 583 76">
        <polygon points="0,20 200,0 583,0 583,28 150,40 0,45" fill="var(--orange-light)" opacity="0.55"/>
        <rect x="150" y="30" width="200" height="18" fill="var(--orange-deep)" opacity="0.5"/>
        <rect x="380" y="10" width="120" height="30" fill="#f9b46a" opacity="0.4"/>
        <polygon points="0,60 583,50 583,76 0,76" fill="var(--orange-deep)" opacity="0.7"/>
      </svg>
      <p class="web-address">www.venmoretranslinks.com</p>
    </div>
    <div class="base-strip"></div>
  </section>

  <!-- Inside right page -->
  <section class="page page--right">
    <div class="photo" role="img" aria-label="Studio microphone with pop filter in a voice-over booth" style="left:42px; top:84px; width:230px; height:150px; background:linear-gradient(135deg,#1b1b1b,#555 50%,#2a2a2a);"></div>
    <div class="band">
      <div class="band__panel" style="width:215px;">
        <p style="top:50px;">MEETINGS:<br>LET EVERYONE<br>SPEAK,<br>AND BE<br>UNDERSTOOD
          <svg width="40" height="14" viewBox="0 0 40 14"><circle cx="6" cy="7" r="4.5" fill="var(--white)"/><circle cx="20" cy="7" r="5.5" fill="var(--white)"/><circle cx="33" cy="7" r="3" fill="var(--white)"/></svg></p>
      </div>
      <div class="band__photo" role="img" aria-label="Boardroom table set for a meeting with white chairs" style="left:215px; width:368px; background:linear-gradient(160deg,#3a2410,#8a5a2a 45%,#c9a070 80%,#e8d8c0);"></div>
    </div>
    <div class="rule"></div>
    <div class="footer-band">
      <svg width="583" height="76" viewBox="0 0 583 76">
        <rect x="120" y="0" width="30" height="76" fill="var(--orange-deep)" opacity="0.6"/>
        <rect x="260" y="0" width="18" height="76" fill="var(--orange-light)" opacity="0.6"/>
        <rect x="300" y="0" width="40" height="76" fill="var(--orange-deep)" opacity="0.45"/>
        <rect x="430" y="0" width="22" height="76" fill="#f9b46a" opacity="0.5"/>
        <polygon points="0,60 583,50 583,76 0,76" fill="var(--orange-deep)" opacity="0.6"/>
      </svg>
      <p class="web-address">www.venmoretranslinks.com</p>
    </div>
    <div class="base-strip"></div>
  </section>

  <h1 class="feature-title">IN HOUSE<br>VOICE-OVER<br>AND SUBTITLING<br>SERVICES
    <svg width="40" height="14" viewBox="0 0 40 14"><circle cx="5" cy="7" r="4" fill="var(--orange)"/><circle cx="19" cy="7" r="5.5" fill="var(--orange-light)"/><circle cx="33" cy="7" r="3" fill="var(--orange)"/></svg></h1>
  <p class="body-copy" style="left:620px; top:271px; width:540px;">“Language Solutions” are the services that allow communication to transcend language barriers. We begin with translators and interpreters and finish with the technology to bring it all together. Our solutions are just that: answers to problems. We meet your needs so you don't have to worry. Through Venmore, youcommunicate with your global audience with equal respect. We are a nationwide leader in live event language services, which includes simultaneous interpreters, interpreting equipment, and push-to-talk discussion systems. Our translation division has decades of experience and millions of words under its belt. Today, these services include a full range of studio services like voiceover and subtitles.</p>
</div>

</body>
</html>
```